Paws and Meadows is a dog walking service that offers home boarding and pet taxi

I am looking for a eye catching A5 leaflet/flyer design for my dog walking business Paws and Meadows.

The flyer must have my company logo on it (jpeg), a picture of my van (jpeg) and a picture of dogs playing (jpegs 1-5).

The fonts must be easy to read. I am not set on any colour scheme but do like the idea of having a natural background. IE. Green grass and blue sky or some forest setting with green trees. If you don't like this idea or its hard to work with don't worry I am open minded so be creative and do what you thinks best.

I'll provide quick feedback to designs that i like and so we can work together.

The flyers must contain the following:

60 minute group and individual walks
GPS Tracked Walks
Home Boarding
Pet Taxi
Puppy/Pet visits

Offer: 50% off first weeks dogs walks with this flyer.

As well as containing my contact info:

07519306284
www.pawsmeadowsgroup.co.uk
pawsmeadowsgroup@brightmailbox.co.uk

Chatterbook, Quipster and Snapfolio logos must be present as well.

Thanks and Good luck!

Target Market(s)

ANYONE WHO NEEDS THEIR DOG WALKED OR LOOKED AFTER WHEN THEY ARE ON HOLIDAY

Industry/Entity Type

Business

Contact Information for Business Card

THE BUSINESS CARD MUST DISPLAY THE LOGO THAT HAS BEEN UPLOADED IN A FILE. IT MUST LOOK SHARP AND PROFESSIONAL. CONTAIN ALL CONTACT INFO AND HAVE SERVICES OFFERED. SEE PROJECT DESCRIPTION FOR FLYER.

Font styles to use
Serif
Sans Serif

Requirements
Must have
• SEE PROJECT DESCRIPTION
Nice to have
• IT WOULD BE NICE TO HAVE PHOTOS OF MY VAN AND DOGS PLAYING. I HAVE UPLOADED SOME PICS OF VAN TO BE USED AND THERE ARE PICS OF DOGS PLAYING THAT COULD BE USED.

```html
<!DOCTYPE html>
<html lang="en">
<head>
<meta charset="utf-8">
<title>Paws and Meadows – Dog Walking Flyer</title>
<link rel="stylesheet" href="https://fonts.googleapis.com/css2?family=Anton&family=Arimo:wght@400;600;700&family=Bebas+Neue&display=swap">
<style>
  :root {
    --sun: #fbf8c8;
    --meadow-light: #cfe04e;
    --meadow: #86b82c;
    --meadow-deep: #3f7d1c;
    --sky-blue: #1ea0e4;
    --navy-blue: #1d4aa8;
    --icon-blue: #1e6ec8;
    --orange: #f29414;
    --offer-red: #e0202e;
    --ink: #151515;
    --white: #ffffff;
  }
  * { margin: 0; padding: 0; box-sizing: border-box; }
  html, body { width: 838px; height: 1200px; overflow: hidden; background: #ffffff; }
  .flyer {
    position: relative;
    width: 838px;
    height: 1200px;
    overflow: hidden;
    font-family: "Bebas Neue", sans-serif;
  }
  .meadow-backdrop {
    position: absolute; inset: 0;
    background:
      radial-gradient(ellipse 420px 320px at 260px 40px, var(--sun) 0%, rgba(251,248,200,0) 100%),
      radial-gradient(ellipse 300px 260px at 700px 820px, rgba(250,250,240,0.35) 0%, rgba(250,250,240,0) 100%),
      linear-gradient(180deg, #e6ea8c 0%, var(--meadow-light) 32%, var(--meadow) 58%, var(--meadow-deep) 100%);
  }
  .diagonal-bands { position: absolute; inset: 0; width: 838px; height: 1200px; }

  .brand {
    position: absolute; top: 50px; left: 0; width: 838px;
    display: flex; flex-direction: column; align-items: center;
  }
  .brand-mark {
    width: 132px; height: 132px; border-radius: 50%;
    background: var(--orange);
  }
  .brand-name {
    margin-top: 12px;
    font-family: "Bebas Neue", sans-serif;
    font-size: 50px; letter-spacing: 2px; color: var(--ink); line-height: 1;
  }
  .brand-tagline {
    margin-top: 2px;
    font-family: "Arimo", sans-serif; font-size: 11px; letter-spacing: 2px;
    text-transform: uppercase; color: var(--ink);
  }

  .service { position: absolute; display: flex; align-items: flex-start; gap: 10px; }
  .service-icon { flex: none; }
  .service-label { font-size: 33px; line-height: 0.82; color: var(--ink); padding-top: 2px; }
  .service--walks  { left: 80px;  top: 300px; }
  .service--gps    { left: 355px; top: 300px; }
  .service--board  { left: 572px; top: 300px; }
  .service--taxi   { left: 228px; top: 440px; }
  .service--visits { left: 446px; top: 440px; }

  .offer-burst {
    position: absolute; left: 28px; top: 530px;
    width: 210px; height: 185px;
    background: var(--offer-red);
    border: 8px solid var(--white);
    transform: rotate(-14deg);
    display: flex; flex-direction: column; justify-content: center; align-items: center;
  }
  .offer-figure { font-family: "Anton", sans-serif; color: var(--white); font-size: 70px; line-height: 0.95; }
  .offer-terms {
    position: absolute; left: 50px; top: 750px;
    color: var(--white); font-size: 23px; line-height: 0.9;
  }
  .offer-terms span { display: block; padding-left: 12px; }
  .offer-terms span:first-child { padding-left: 0; }

  .photo { position: absolute; }
  .photo--van {
    left: 205px; top: 762px; width: 548px; height: 270px;
    border-radius: 14px 70px 40px 14px;
    background:
      radial-gradient(ellipse 180px 120px at 30% 40%, rgba(70,120,200,0.85) 0%, rgba(70,120,200,0) 100%),
      radial-gradient(ellipse 220px 90px at 35% 85%, rgba(90,160,70,0.8) 0%, rgba(90,160,70,0) 100%),
      linear-gradient(180deg, #f2f3f5 0%, #e4e6ea 100%);
    box-shadow: 0 6px 14px rgba(0,0,0,0.18);
  }
  .photo--dogs {
    left: 0; top: 838px; width: 384px; height: 362px;
    border-radius: 150px 160px 0 0;
    background:
      radial-gradient(ellipse 140px 200px at 30% 45%, #2a2a2a 0%, rgba(42,42,42,0) 100%),
      radial-gradient(ellipse 130px 200px at 72% 45%, #d8b47c 0%, rgba(216,180,124,0) 100%),
      linear-gradient(90deg, #3a3530 0%, #8d7350 55%, #c9a470 100%);
  }

  .contact {
    position: absolute; left: 395px; top: 1037px; width: 330px;
    text-align: center; color: var(--white);
    font-family: "Arimo", sans-serif; font-weight: 600; font-style: normal;
    font-size: 19px; line-height: 24px;
  }
  .contact-email { font-size: 16px; }
  .social {
    position: absolute; left: 395px; top: 1132px; width: 330px;
    display: flex; justify-content: center; gap: 18px;
    font-family: "Arimo", sans-serif; font-weight: 700;
    font-size: 16px; color: var(--white);
  }
</style>
</head>
<body>
<main class="flyer">
  <div class="meadow-backdrop" role="img" aria-label="Sunlit meadow of green grass with white wildflowers and a bright sun haze"></div>

  <svg class="diagonal-bands" viewBox="0 0 838 1200" aria-hidden="true">
    <polygon points="0,364 810,1200 0,1200" fill="var(--sky-blue)"/>
    <polygon points="0,616 560,1200 0,1200" fill="var(--orange)"/>
    <polygon points="420,1200 520,1010 790,1160 810,1200" fill="var(--navy-blue)" opacity="0.92"/>
  </svg>

  <header class="brand">
    <span class="brand-mark"></span>
    <span class="brand-name">Paws and Meadows</span>
    <span class="brand-tagline">Dog walking service</span>
  </header>

  <div class="service service--walks">
    <svg class="service-icon" width="56" height="60" viewBox="0 0 56 60">
      <rect x="22" y="0" width="12" height="6" rx="2" fill="var(--icon-blue)"/>
      <circle cx="28" cy="34" r="25" fill="var(--icon-blue)"/>
      <circle cx="28" cy="34" r="20" fill="none" stroke="#ffffff" stroke-width="2"/>
      <text x="28" y="45" text-anchor="middle" font-family="Bebas Neue, sans-serif" font-size="30" fill="#f4d400">60</text>
    </svg>
    <p class="service-label">60 minute<br>group and<br>individual<br>walks</p>
  </div>

  <div class="service service--gps">
    <svg class="service-icon" width="46" height="62" viewBox="0 0 46 62">
      <path d="M23 0 C10 0 0 10 0 23 C0 40 23 62 23 62 C23 62 46 40 46 23 C46 10 36 0 23 0 Z" fill="var(--icon-blue)"/>
      <circle cx="23" cy="22" r="8" fill="#ffffff"/>
    </svg>
    <p class="service-label">GPS<br>tracked<br>walks</p>
  </div>

  <div class="service service--board">
    <svg class="service-icon" width="66" height="62" viewBox="0 0 66 62">
      <polygon points="33,0 66,30 57,30 57,62 9,62 9,30 0,30" fill="var(--icon-blue)"/>
      <rect x="25" y="34" width="16" height="16" rx="3" fill="#ffffff"/>
    </svg>
    <p class="service-label">Home<br>boarding</p>
  </div>

  <div class="service service--taxi">
    <svg class="service-icon" width="104" height="62" viewBox="0 0 104 62">
      <rect x="24" y="0" width="56" height="24" rx="10" fill="var(--icon-blue)"/>
      <text x="52" y="19" text-anchor="middle" font-family="Bebas Neue, sans-serif" font-size="20" fill="#f4d400">TAXI</text>
      <path d="M10 62 L20 40 Q22 34 30 34 L74 34 Q82 34 84 40 L94 62 Z" fill="var(--icon-blue)"/>
    </svg>
    <p class="service-label">Pet<br>taxi</p>
  </div>

  <div class="service service--visits">
    <svg class="service-icon" width="72" height="64" viewBox="0 0 72 64">
      <path d="M36 64 L6 34 C-4 22 2 2 20 2 C28 2 33 7 36 12 C39 7 44 2 52 2 C70 2 76 22 66 34 Z" fill="var(--icon-blue)"/>
    </svg>
    <p class="service-label">Puppy/pet<br>visits</p>
  </div>

  <div class="offer-burst">
    <span class="offer-figure">50%</span>
    <span class="offer-figure">OFF</span>
  </div>
  <p class="offer-terms">
    <span>*First week</span>
    <span>dog walks</span>
    <span>with this flyer</span>
  </p>

  <div class="photo photo--van" role="img" aria-label="Photo of the company's white branded van with a roof rack"></div>
  <div class="photo photo--dogs" role="img" aria-label="Photo of a black dog and a golden dog running together carrying a stick"></div>

  <address class="contact">
    <p class="contact-phone">07519306284</p>
    <p class="contact-web">www.pawsmeadowsgroup.co.uk</p>
    <p class="contact-email">pawsmeadowsgroup@brightmailbox.co.uk</p>
  </address>

  <nav class="social">
    <span>Chatterbook</span>
    <span>Quipster</span>
    <span>Snapfolio</span>
  </nav>
</main>
</body>
</html>
```